business card for law firm that reflects the web site -www.MarlaQuentby.com. That is pleasant to read

We need a business card for a small law firm. Your company designed our logo - tree of life - which I can provide to the designers. The card should be on both sides. Use the coloring from the web site (www.MarlaQuentby.com) and logo (I have several formats). I am attaching the logo, but not sure what format to use.

First side name of firm: Law Office of M.K. Quentby, P.A. 4819 West Pallisor, Suite 300, Phoenix, AZ 85016, Phone: 602.555.3841, Fax: 602.555.7290, web site: www.MarlaQuentby.com, email: MQuentby@MarlaQuentby.com.
Marla K. Quentby Bankruptcy and Foreclosure Attorney & Counselor.
Back side (perhaps vertical) the logo and then Notes with lines. At the bottom: Proud to help people and small businesses file for bankruptcy protection. We are a debt relief agency.
Updates

I have several versions of the logo. Will be happy to share whatever you need. Added Sunday, April 3, 2016

Target Market(s)

everyone

Industry/Entity Type

Legal

Contact Information for Business Card

I prefer something unique (rounded edges, design that adopts my web site - www.MarlaQuentby.com.

Font styles to use
Serif

Requirements
Must have
• First side name of firm: Law Office of M.K. Quentby, P.A. 4819 West Pallisor, Suite 300, Phoenix, AZ 85016, Phone: 602.555.3841, Fax: 602.555.7290, web site: www.MarlaQuentby.com, email: MQuentby@MarlaQuentby.com.
• Marla K. Quentby Bankruptcy and Foreclosure Attorney & Counselor.
• Back side (perhaps vertical) the logo and then Notes with lines. At the bottom: Proud to help people and small businesses file for bankruptcy protection. We are a debt relief agency.
• Green and brown colors that reflect the web site: www.MarlaQuentby.com
Should not have
• Type so small that older people cannot read.

```html
<!DOCTYPE html>
<html lang="en">
<head>
<meta charset="utf-8">
<title>Law Office of M.K. Quentby, P.A. — Business Card</title>
<link rel="stylesheet" href="https://fonts.googleapis.com/css2?family=Open+Sans:wght@400;700&display=swap">
<style>
  :root {
    --bg: #e9eaec;
    --brown: #3a1c0c;
    --green: #0f4a14;
    --green-icon: #1d5a22;
    --white: #ffffff;
    --ink: #2b2b2b;
    --rule: #d6d6d6;
  }
  * { margin: 0; padding: 0; box-sizing: border-box; }
  html, body { width: 1200px; height: 801px; overflow: hidden; }
  body {
    background: var(--bg);
    font-family: "Open Sans", Arial, sans-serif;
    color: var(--ink);
    position: relative;
  }
  .card {
    position: absolute;
    width: 540px;
    height: 308px;
    box-shadow: 0 6px 18px rgba(0,0,0,0.18);
    overflow: hidden;
  }

  /* Back side */
  .card-back { left: 50px; top: 90px; background: var(--brown); }
  .card-back .brand {
    position: absolute; left: 0; right: 0; top: 52px;
    display: flex; flex-direction: column; align-items: center; gap: 12px;
  }
  .brand-mark {
    width: 130px; height: 130px; border-radius: 50%;
    background: var(--green);
  }
  .card-back .brand-name { font-size: 18px; font-weight: 700; color: var(--white); letter-spacing: 0.5px; }
  .card-back .web { position: absolute; left: 0; right: 0; top: 250px; text-align: center; color: var(--white); font-size: 17px; letter-spacing: 0.5px; }
  .card-back .base-band { position: absolute; left: 0; right: 0; bottom: 0; height: 12px; background: var(--green); }

  /* Front side */
  .card-front { left: 610px; top: 330px; background: var(--white); }
  .card-front .top-band { position: absolute; left: 0; right: 0; top: 0; height: 14px; background: var(--brown); }
  .card-front .brand {
    position: absolute; left: 34px; top: 52px; width: 170px;
    display: flex; flex-direction: column; align-items: center; gap: 10px;
  }
  .card-front .brand-mark { width: 140px; height: 140px; border: 6px solid var(--brown); }
  .card-front .brand-name { font-size: 15px; font-weight: 700; color: var(--brown); }
  .divider { position: absolute; left: 232px; top: 44px; width: 1px; height: 168px; background: var(--rule); }
  .firm { position: absolute; left: 250px; top: 46px; width: 280px; }
  .firm-name { font-size: 19px; font-weight: 700; line-height: 1.1; text-transform: uppercase; color: #1f1f1f; }
  .contacts { list-style: none; margin-top: 14px; }
  .contacts li { display: flex; align-items: flex-start; gap: 10px; font-size: 12.5px; line-height: 1.25; margin-bottom: 6px; }
  .contacts svg { flex: none; width: 16px; height: 16px; margin-top: 1px; }
  .tagline { position: absolute; left: 24px; top: 250px; font-size: 12.5px; color: #333; }
  .accent-green { position: absolute; left: 0; width: 66%; top: 235px; height: 6px; background: var(--green); }
  .accent-brown { position: absolute; right: 0; width: 33%; top: 229px; height: 12px; background: var(--brown); }
  .base-band { position: absolute; left: 0; right: 0; bottom: 0; height: 12px; background: var(--green); }

  /* Standalone mark */
  .standalone { position: absolute; left: 50px; top: 560px; display: flex; align-items: center; gap: 16px; }
  .standalone .brand-mark { width: 150px; height: 150px; border: 8px solid var(--brown); }
  .standalone .brand-name { font-size: 20px; font-weight: 700; color: var(--brown); }
</style>
</head>
<body>

  <section class="card card-back" aria-label="Business card back">
    <div class="brand">
      <div class="brand-mark"></div>
      <span class="brand-name">M.K. Quentby</span>
    </div>
    <p class="web">www.MarlaQuentby.com</p>
    <div class="base-band"></div>
  </section>

  <section class="card card-front" aria-label="Business card front">
    <div class="top-band"></div>
    <div class="brand">
      <div class="brand-mark"></div>
      <span class="brand-name">M.K. Quentby</span>
    </div>
    <div class="divider"></div>
    <div class="firm">
      <h1 class="firm-name">Law Office of<br>M.K. Quentby, P.A</h1>
      <ul class="contacts">
        <li>
          <svg viewBox="0 0 16 16"><circle cx="8" cy="8" r="7.3" fill="none" stroke="var(--green-icon)" stroke-width="1.2"/><path d="M5.5 4.5l1.4 1.6-.8 1c.5 1 1.3 1.8 2.3 2.3l1-.8 1.6 1.4-.9 1.2c-2.6-.4-4.6-2.4-5-5z" fill="var(--green-icon)"/></svg>
          <span>602.555.3841</span>
        </li>
        <li>
          <svg viewBox="0 0 16 16"><circle cx="8" cy="8" r="7.3" fill="none" stroke="var(--green-icon)" stroke-width="1.2"/><rect x="4.5" y="6" width="7" height="5" rx="0.6" fill="var(--green-icon)"/><rect x="6" y="4" width="4" height="2.2" fill="var(--green-icon)"/></svg>
          <span>602.555.7290</span>
        </li>
        <li>
          <svg viewBox="0 0 16 16"><circle cx="8" cy="8" r="7.3" fill="none" stroke="var(--green-icon)" stroke-width="1.2"/><rect x="4.3" y="5.3" width="7.4" height="5.4" fill="var(--green-icon)"/><path d="M4.5 5.6L8 8.4l3.5-2.8" fill="none" stroke="#fff" stroke-width="0.9"/></svg>
          <span>MQuentby@MarlaQuentby.com</span>
        </li>
        <li>
          <svg viewBox="0 0 16 16"><circle cx="8" cy="8" r="7.3" fill="none" stroke="var(--green-icon)" stroke-width="1.2"/><path d="M8 12.5s-3-3.2-3-5.3a3 3 0 016 0c0 2.1-3 5.3-3 5.3z" fill="var(--green-icon)"/><circle cx="8" cy="7.2" r="1.1" fill="#fff"/></svg>
          <span>4819 West Pallisor, Suite 300,<br>Phoenix, AZ 85016,</span>
        </li>
      </ul>
    </div>
    <div class="accent-brown"></div>
    <div class="accent-green"></div>
    <p class="tagline">Marla K. Quentby Bankruptcy and Foreclosure Attorney &amp; Counselor.</p>
    <div class="base-band"></div>
  </section>

  <div class="standalone">
    <div class="brand-mark"></div>
    <span class="brand-name">M.K. Quentby</span>
  </div>

</body>
</html>
```